Small company security and risk consulting startup needs an explosive message via marketing colla...

Need a two page (front/back) flyer that calls out our three primary service areas incorporating brandmill developed logo and website visuals. Something that grabs attention at first glance to entice the viewer to read and connect for a services consultation. I will need the ability to make minor adjustments and add language.

```html
<!DOCTYPE html>
<html lang="en">
<head>
<meta charset="utf-8">
<title>Ironvale Security – Consulting Service Flyer</title>
<link href="https://fonts.googleapis.com/css2?family=Roboto:wght@300;400;700&family=Didact+Gothic&display=swap" rel="stylesheet">
<style>
  :root{
    --backdrop:#e4e2de;
    --paper:#f3f3f3;
    --navy:#1f2f80;
    --navy-deep:#0c1552;
    --red:#d91c24;
    --red-dark:#6e070b;
    --charcoal:#222325;
    --ink:#333;
    --muted:#8a8a8a;
    --band-gray:#e1e1e3;
    --white:#fff;
  }
  *{margin:0;padding:0;box-sizing:border-box}
  html,body{width:1200px;height:795px;overflow:hidden;background:var(--backdrop)}
  body{position:relative;font-family:"Didact Gothic",sans-serif;color:var(--ink)}
  .page{position:absolute;top:96px;width:460px;height:596px;background:var(--paper);overflow:hidden;box-shadow:0 1px 4px rgba(0,0,0,.15)}
  .page--front{left:147px}
  .page--back{left:647px}
  .layer{position:absolute;left:0;top:0}
  .abs{position:absolute}

  /* front hero */
  .hero-title{left:27px;top:57px;font-family:"Roboto",sans-serif;font-weight:700;font-size:29px;line-height:31px;color:var(--white);letter-spacing:.3px}
  .hero-rule{left:27px;top:125px;width:46px;height:2px;background:var(--white)}
  .values{left:27px;top:146px;list-style:none;font-family:"Roboto",sans-serif;font-weight:300;font-size:10.5px;color:var(--white);line-height:17.6px}
  .values li::before{content:"•";margin-right:3px}
  .brand{font-family:"Roboto",sans-serif;font-weight:700;color:var(--red);text-align:center;white-space:nowrap}
  .brand-tagline{font-size:3.6px;color:var(--red);letter-spacing:.8px;text-align:center;white-space:nowrap}
  .front-brand{left:157px;top:229px;width:170px;font-size:12px}
  .front-tagline{left:157px;top:246px;width:170px}

  /* services */
  .service{position:absolute;top:297px;text-align:center;color:var(--white);font-family:"Roboto",sans-serif}
  .service svg{display:block;margin:0 auto 5px}
  .service-kind{font-weight:300;font-size:8.2px;letter-spacing:.4px}
  .service-name{font-weight:700;font-size:8.6px;letter-spacing:.5px;margin-top:1px}
  .service-note{font-family:"Didact Gothic",sans-serif;font-size:4.6px;line-height:6.4px;margin:5px auto 0}

  /* text columns */
  .section-head{font-family:"Roboto",sans-serif;font-size:12.5px;color:var(--ink);letter-spacing:.2px}
  .section-head b{font-weight:700}
  .section-head span{font-weight:300}
  .body-copy{font-size:6.7px;line-height:9px;color:var(--muted)}
  .col-about{left:28px;top:429px;width:170px}
  .col-why{left:250px;top:429px;width:170px}
  .col-about .body-copy,.col-why .body-copy{margin-top:7px}
  .divider{left:225px;top:423px;height:78px;border-left:1px dashed #9a9a9a}

  /* footers */
  .footer{position:absolute;left:0;width:460px;background:var(--charcoal);color:#e8e8e8;font-size:7.2px}
  .footer--front{top:517px;height:79px}
  .footer--back{top:563px;height:33px}
  .contact{position:absolute;display:flex;align-items:flex-start;gap:6px;line-height:9px;white-space:nowrap}
  .contact svg{flex:none;margin-top:0}
  .social{position:absolute;top:563px;width:16px;height:16px;border:1.2px solid #ddd;border-radius:50%}

  /* back */
  .header-values{left:200px;top:34px;font-family:"Roboto",sans-serif;font-size:12px;color:var(--red);word-spacing:2px;white-space:nowrap}
  .header-values i{font-style:normal;font-size:9px;margin:0 2px 0 10px}
  .back-brand{left:20px;top:48px;width:150px;font-size:10.5px}
  .back-tagline{left:20px;top:62px;width:150px}
  .why-title{left:30px;top:150px;font-family:"Roboto",sans-serif;font-size:24px;color:var(--white)}
  .why-title b{font-weight:700}
  .why-title span{font-weight:300}
  .why-copy{left:30px;top:186px;width:170px;color:var(--white)}
  .feature-frame{left:125px;top:390px;width:314px;height:134px;border:4px solid var(--navy);background:var(--paper)}
  .feature-photo{left:30px;top:373px;width:202px;height:168px;background:linear-gradient(135deg,#d7d4cf,#bdb6ad 55%,#8d8276)}
  .feature-head{left:254px;top:419px;font-family:"Roboto",sans-serif;font-weight:700;font-size:12.5px;color:var(--ink)}
  .feature-copy{left:254px;top:442px;width:170px}
</style>
</head>
<body>

<!-- FRONT -->
<section class="page page--front">
  <svg class="layer" width="460" height="596" viewBox="0 0 460 596">
    <defs>
      <linearGradient id="heroBlue" x1="0" y1="0" x2="1" y2="1">
        <stop offset="0" stop-color="#1d2c8a"/><stop offset=".6" stop-color="#142070"/><stop offset="1" stop-color="#070d3a"/>
      </linearGradient>
      <linearGradient id="meetingGray" x1="0" y1="0" x2="1" y2="1">
        <stop offset="0" stop-color="#e9e9e9"/><stop offset=".55" stop-color="#9d9d9d"/><stop offset="1" stop-color="#3a3a3a"/>
      </linearGradient>
      <linearGradient id="cardDark" x1="0" y1="0" x2="0" y2="1"><stop offset="0" stop-color="#3a3a3c"/><stop offset="1" stop-color="#1b1b1c"/></linearGradient>
      <linearGradient id="cardRed" x1="0" y1="0" x2="0" y2="1"><stop offset="0" stop-color="#e0222a"/><stop offset="1" stop-color="#6e070b"/></linearGradient>
      <linearGradient id="cardBlue" x1="0" y1="0" x2="0" y2="1"><stop offset="0" stop-color="#25389a"/><stop offset="1" stop-color="#18256d"/></linearGradient>
    </defs>
    <rect role="img" aria-label="Black and white photo of three business people talking beside a conference table" x="236" y="0" width="224" height="255" fill="url(#meetingGray)"/>
    <polygon role="img" aria-label="Blue-toned photo of a businessman with rising arrows" points="0,0 330,0 147,255 0,255" fill="url(#heroBlue)"/>
    <polygon points="330,0 346,0 256,126 337,255 322,255 236,126" fill="var(--red)"/>
    <polygon points="243,126 147,255 333,255" fill="var(--paper)"/>
    <polygon points="0,287 87,287 28,403 0,403" fill="var(--band-gray)"/>
    <polygon points="366,287 460,287 460,403 428,403" fill="var(--band-gray)"/>
    <polygon points="87,287 147,287 204,403 28,403" fill="url(#cardDark)"/>
    <polygon points="147,287 314,287 263,403 213,403" fill="url(#cardRed)"/>
    <polygon points="314,287 366,287 428,403 255,403" fill="url(#cardBlue)"/>
  </svg>

  <h1 class="abs hero-title">CONSULTING<br>SERVICE</h1>
  <div class="abs hero-rule"></div>
  <ul class="abs values"><li>COMMITMENT</li><li>INTEGRITY</li><li>RESULTS</li></ul>

  <div class="abs brand front-brand">Ironvale Security</div>
  <div class="abs brand-tagline front-tagline">commitment · integrity · results</div>

  <div class="service" style="left:64px;width:106px">
    <svg width="24" height="22" viewBox="0 0 24 22" fill="none" stroke="#fff" stroke-width="1.2"><rect x="1" y="1" width="18" height="13"/><path d="M7 18h6M10 14v4"/><rect x="16" y="8" width="7" height="12"/></svg>
    <div class="service-kind">NATIONAL</div>
    <div class="service-name">SECURITY</div>
    <p class="service-note">With a policy of recruiting only<br>the highest caliber members</p>
  </div>
  <div class="service" style="left:180px;width:100px">
    <svg width="22" height="24" viewBox="0 0 22 24" fill="none" stroke="#fff" stroke-width="1.2"><rect x="2" y="1" width="13" height="22" rx="1.5"/><path d="M2 4h13M2 19h13"/><rect x="11" y="11" width="8" height="7"/><path d="M13 11V9a2 2 0 0 1 4 0v2"/></svg>
    <div class="service-kind">RISK MANAGEMENT</div>
    <div class="service-name">SERVICES</div>
    <p class="service-note" style="width:54px">With a policy of recruiting only the highest caliber members</p>
  </div>
  <div class="service" style="left:290px;width:100px">
    <svg width="24" height="22" viewBox="0 0 24 22" fill="none" stroke="#fff" stroke-width="1.2"><path d="M6 1h17v11h-3v3l-3-3H6z"/><path d="M1 6h4v10h3v3l3-3h6"/><path d="M9 5h10M9 8h10"/></svg>
    <div class="service-kind">CONSULTING</div>
    <div class="service-name">SERVICES</div>
    <p class="service-note">With a policy of recruiting only<br>the highest caliber members</p>
  </div>

  <div class="abs col-about">
    <h2 class="section-head"><b>ABOUT</b> <span>US</span></h2>
    <p class="body-copy">Lorem ipsum dolor sit amet, consectetuer adipiscing elit, sed diam nonummy nibh euismod tincidunt ut laoreet dolore magna aliquam erat volutpat. Ut wisi enim ad minim veniam, quis nostrud exerci tation</p>
  </div>
  <div class="abs divider"></div>
  <div class="abs col-why">
    <h2 class="section-head"><b>WHY</b> <span>WE ARE</span></h2>
    <p class="body-copy">Lorem ipsum dolor sit amet, consectetuer adipiscing elit, sed diam nonummy nibh euismod tincidunt ut laoreet dolore magna aliquam erat volutpat. Ut wisi enim ad minim veniam, quis nostrud exerci tation</p>
  </div>

  <footer class="footer footer--front">
    <div class="contact" style="left:30px;top:18px">
      <svg width="8" height="10" viewBox="0 0 8 10"><path d="M4 0a4 4 0 0 1 4 4c0 3-4 6-4 6S0 7 0 4a4 4 0 0 1 4-4z" fill="#eee"/><circle cx="4" cy="4" r="1.5" fill="var(--charcoal)"/></svg>
      <span>48 Harbor Lane, Suite 2B<br>Austin TX 78701</span>
    </div>
    <div class="contact" style="left:179px;top:18px">
      <svg width="9" height="7" viewBox="0 0 9 7" fill="none" stroke="#eee"><rect x=".5" y=".5" width="8" height="6"/><path d="M.5 .5l4 3.5 4-3.5"/></svg><span>hello@ironvale.co</span>
    </div>
    <div class="contact" style="left:179px;top:34px">
      <svg width="8" height="8" viewBox="0 0 8 8"><path d="M1 0h2l1 2-1.2 1a5 5 0 0 0 2.2 2.2L6 4l2 1v2a1 1 0 0 1-1 1A7 7 0 0 1 0 1a1 1 0 0 1 1-1z" fill="#eee"/></svg><span>(555) 014 2290</span>
    </div>
    <div class="contact" style="left:179px;top:50px">
      <svg width="8" height="8" viewBox="0 0 8 8" fill="none" stroke="#eee" stroke-width=".8"><circle cx="4" cy="4" r="3.5"/><path d="M.5 4h7M4 .5c-2 2-2 5 0 7M4 .5c2 2 2 5 0 7"/></svg><span>www.ironvale.co</span>
    </div>
    <svg class="abs" style="left:337px;top:-7px" width="68" height="86" viewBox="0 0 68 86">
      <path d="M0 0h68v68L34 86 0 68z" fill="var(--red)"/>
      <circle cx="34" cy="41" r="27" fill="var(--white)"/>
      <circle cx="34" cy="41" r="20" fill="none" stroke="var(--navy)" stroke-width="3"/>
    </svg>
  </footer>
  <span class="social" style="left:29px"></span>
  <span class="social" style="left:57px"></span>
  <span class="social" style="left:86px"></span>
</section>

<!-- BACK -->
<section class="page page--back">
  <svg class="layer" width="460" height="596" viewBox="0 0 460 596">
    <defs>
      <linearGradient id="deskGray" x1="0" y1="0" x2="1" y2="1">
        <stop offset="0" stop-color="#cfcfcf"/><stop offset=".5" stop-color="#8e8e8e"/><stop offset="1" stop-color="#e2e2e2"/>
      </linearGradient>
      <linearGradient id="whyRed" x1="0" y1="0" x2="1" y2="0">
        <stop offset="0" stop-color="#e0222a"/><stop offset=".6" stop-color="#b8121a"/><stop offset="1" stop-color="#6a0509"/>
      </linearGradient>
    </defs>
    <rect role="img" aria-label="Black and white photo of hands working with financial charts and a calculator" x="0" y="86" width="460" height="247" fill="url(#deskGray)"/>
    <polygon points="0,86 341,86 136,333 0,333" fill="url(#whyRed)"/>
  </svg>

  <div class="abs brand back-brand">Ironvale Security</div>
  <div class="abs brand-tagline back-tagline">commitment · integrity · results</div>
  <div class="abs header-values"><i>•</i>commitment <i>•</i>integrity <i>•</i>results</div>

  <h2 class="abs why-title"><b>WHY</b> <span>WE ARE</span></h2>
  <p class="abs body-copy why-copy">Lorem ipsum dolor sit amet, consectetuer adipiscing elit, sed diam nonummy nibh euismod tincidunt ut laoreet dolore magna aliquam erat volutpat. Ut wisi enim ad minim veniam, quis nostrud exerci tation</p>

  <div class="abs feature-frame"></div>
  <div class="abs feature-photo" role="img" aria-label="Photo of a business team meeting around a conference table"></div>
  <h3 class="abs feature-head">Lorem ipsum dolor sit</h3>
  <p class="abs body-copy feature-copy">Lorem ipsum dolor sit amet, consectetuer adipiscing elit, sed diam nonummy nibh euismod tincidunt ut laoreet dolore magna aliquam erat volutpat. Ut wisi enim ad minim veniam, quis nostrud exerci tation</p>

  <footer class="footer footer--back">
    <div class="contact" style="left:31px;top:12px">
      <svg width="9" height="7" viewBox="0 0 9 7" fill="none" stroke="#eee"><rect x=".5" y=".5" width="8" height="6"/><path d="M.5 .5l4 3.5 4-3.5"/></svg><span>hello@ironvale.co</span>
    </div>
    <div class="contact" style="left:181px;top:12px">
      <svg width="8" height="8" viewBox="0 0 8 8" fill="none" stroke="#eee" stroke-width=".8"><circle cx="4" cy="4" r="3.5"/><path d="M.5 4h7M4 .5c-2 2-2 5 0 7M4 .5c2 2 2 5 0 7"/></svg><span>www.ironvale.co</span>
    </div>
    <div class="contact" style="left:319px;top:12px">
      <svg width="8" height="8" viewBox="0 0 8 8"><path d="M1 0h2l1 2-1.2 1a5 5 0 0 0 2.2 2.2L6 4l2 1v2a1 1 0 0 1-1 1A7 7 0 0 1 0 1a1 1 0 0 1 1-1z" fill="#eee"/></svg><span>(555) 014 2290</span>
    </div>
  </footer>
</section>

</body>
</html>
```